Lueur de Provins Immerse in the enchanting flavors of France at Lueur de Provins

A menu that is French in style with the Eiffel Tower. A elegant menu that is in rich blue with red or gold trimmings, we are a French Bakey and Cafe

Target Market(s)

30 to 55 people

Industry/Entity Type

Restaurant

Font styles to use
Decorative

Colors
0054AA
0677BA
7BADD7
CADEEF
E8F1F8
EB3D1F
EC4F4E
F09395
F8D3D4
FCEDEE

Requirements
Must have
• the attachment "My Brunch Specials" is the Menu I want you to create, it has all the text, "My Brunch Special Complete" is a word version. The menu size should be 4 1/4 wide by 14 inches long 2 Sided. must have our logo at the top , Make the font larger, because our biggest complaint about our menu is it is hard to read
Nice to have
• I would love to incorporate the Eiffel Tower as a silhouette in the background
Should not have
• I do not want too many pictures or small print

```html
<!DOCTYPE html>
<html lang="en">
<head>
<meta charset="utf-8">
<title>Lueur de Provins — Brunch &amp; Drink Specials</title>
<link rel="stylesheet" href="https://fonts.googleapis.com/css2?family=Bebas+Neue&family=Cabin:wght@400&family=Montserrat:wght@300;400&family=Oswald:wght@400;600&family=Roboto:wght@700&display=swap">
<style>
  :root{
    --page:#c8c8c8;
    --navy:#13244a;
    --gold:#e2b85a;
    --gold-light:#f5d27a;
    --gold-dark:#c79a3e;
    --red:#df3b33;
    --red-deep:#b8322c;
    --white:#ffffff;
    --ink:#1d1d2b;
  }
  *{box-sizing:border-box;margin:0;padding:0}
  html,body{width:767px;height:1200px;overflow:hidden;background:var(--page)}
  .canvas{position:relative;width:767px;height:1200px}
  .panel{
    position:absolute;top:73px;width:318px;height:1050px;
    background:var(--navy);border:1px solid var(--gold-dark);
    box-shadow:0 6px 14px rgba(0,0,0,.35);overflow:hidden;color:var(--white);
  }
  .panel--brunch{left:44px}
  .panel--drinks{left:396px}
  .backdrop{
    position:absolute;left:0;right:0;bottom:0;height:640px;
    background:linear-gradient(to bottom,rgba(150,40,50,0) 0%,rgba(150,40,50,.18) 55%,rgba(170,45,50,.35) 100%);
  }
  .skyline{
    position:absolute;left:0;right:0;bottom:0;height:46px;
    background:linear-gradient(to bottom,rgba(223,59,51,.35),var(--red-deep));
  }
  .frame{
    position:absolute;left:18px;top:16px;width:284px;height:256px;
    border:1px solid var(--gold);
  }
  .frame svg{position:absolute;left:-1px;top:-1px}
  .brand{position:absolute;left:0;right:0;top:56px;text-align:center}
  .brand__mark{display:block;width:12px;height:12px;margin:0 auto 14px;background:var(--red)}
  .brand__name{
    font-family:"Montserrat",sans-serif;font-weight:400;font-size:11px;
    letter-spacing:5.4px;color:var(--white);padding-left:5px;
  }
  .title{position:absolute;left:0;right:0;text-align:center;font-family:"Bebas Neue",sans-serif;line-height:.8}
  .title__lead{display:block;color:var(--red);text-shadow:0 3px 5px rgba(0,0,0,.45)}
  .title__sub{display:block;color:var(--white);text-shadow:0 3px 5px rgba(0,0,0,.45)}
  .panel--brunch .title{top:130px}
  .panel--brunch .title__lead{font-size:86px;transform:scaleX(.92)}
  .panel--brunch .title__sub{font-size:72px;transform:scaleX(.87);margin-top:1px}
  .panel--drinks .title{top:112px}
  .panel--drinks .title__lead{font-size:118px;transform:scaleX(.78);line-height:.76}
  .panel--drinks .title__sub{font-size:72px;transform:scaleX(.87);margin-top:-2px}
  .menu-word{
    position:absolute;left:50%;transform:translateX(-50%);
    background:var(--navy);padding:0 12px;
    font-family:"Montserrat",sans-serif;font-weight:300;font-size:28px;letter-spacing:5px;line-height:1;
  }
  .panel--brunch .menu-word{top:258px;color:var(--white)}
  .panel--drinks .menu-word{top:254px;color:var(--gold)}
  .item{position:absolute;left:0;right:0;text-align:center}
  .item__head{display:flex;justify-content:center;gap:3px;height:19px}
  .item__name{
    width:162px;height:19px;
    background:linear-gradient(90deg,var(--gold-dark),var(--gold-light) 70%,var(--gold));
    clip-path:polygon(0 0,100% 0,100% 100%,0 100%,7% 50%);
    font-family:"Oswald",sans-serif;font-weight:400;font-size:12.5px;line-height:19px;
    color:var(--ink);padding-left:8px;
  }
  .item__name--wide{width:217px}
  .item__price{
    width:53px;height:19px;background:var(--red);
    clip-path:polygon(0 0,100% 0,84% 50%,100% 100%,0 100%);
    font-family:"Roboto",sans-serif;font-weight:700;font-size:14px;line-height:19px;
    color:var(--white);padding-right:8px;
  }
  .item__desc{
    width:290px;margin:4px auto 0;
    font-family:"Cabin",sans-serif;font-size:7.4px;line-height:10.1px;color:var(--white);
  }
  .section-label{
    position:absolute;left:0;right:0;text-align:center;
    font-family:"Oswald",sans-serif;font-weight:600;font-size:16px;color:var(--red);
  }
</style>
</head>
<body>
<main class="canvas">

  <!-- Brunch side -->
  <section class="panel panel--brunch" aria-label="Brunch specials menu">
    <div class="backdrop" role="img" aria-label="Faint Eiffel Tower silhouettes in the background"></div>
    <div class="skyline" role="img" aria-label="Red Paris skyline silhouette along the bottom edge"></div>

    <div class="frame">
      <svg width="286" height="40" viewBox="0 0 286 40" aria-hidden="true">
        <g stroke="#e2b85a" stroke-width="1" fill="none">
          <line x1="0" y1="37" x2="37" y2="0"/><line x1="0" y1="24" x2="24" y2="0"/>
          <line x1="286" y1="37" x2="249" y2="0"/><line x1="286" y1="24" x2="262" y2="0"/>
        </g>
      </svg>
    </div>

    <div class="brand"><span class="brand__mark"></span><span class="brand__name">LUEUR DE PROVINS</span></div>

    <h1 class="title"><span class="title__lead">BRUNCH</span><span class="title__sub">SPECIALS</span></h1>
    <div class="menu-word">MENU</div>

    <article class="item" style="top:307px">
      <div class="item__head"><h2 class="item__name">RATATOUILLE &amp; EGGS</h2><span class="item__price">$18</span></div>
      <p class="item__desc">Experience the essence of Provence with our Ratatouille, a vibrant medley of roasted squash, peppers, tomatoes, eggplant, infused with fragrant fresh herbs. Served with two perfectly poached eggs, and your choice of flavorful andouille sausage or crispy bacon. Accompanied by a side of crusty baguette. It's a hearty dish that celebrates the flavors of the Mediterranean countryside.</p>
    </article>

    <article class="item" style="top:404px">
      <div class="item__head"><h2 class="item__name">LE GRANDE BREAKFAST</h2><span class="item__price">$15</span></div>
      <p class="item__desc" style="margin-top:13px">Start your day in style with our Le Grande Breakfast, a feast fit for royalty. Customize your morning indulgence with two eggs cooked to your preference, paired with either savory bacon or succulent chicken sausage. Choose between a freshly baked baguette or a buttery croissant to accompany your meal. Complete your breakfast by selecting from an array of sides including crispy hash browns, savory roasted potatoes, or a refreshing fruit salad. Bon appetit!</p>
    </article>

    <article class="item" style="top:512px">
      <div class="item__head"><h2 class="item__name">SMOKED SALMON TARTINE</h2><span class="item__price">$14</span></div>
      <p class="item__desc" style="margin-top:13px">Delight in the luxurious flavors of our Smoked Salmon Tartine, a culinary masterpiece that elevates breakfast to new heights. Indulge in truffled scrambled eggs nestled atop smoked salmon, adorned with tangy pickled red onions, briny caper berries, crisp cucumber, juicy tomato, and peppery arugula. All artfully arranged on multigrain bread generously spread with herb-infused cream cheese.</p>
    </article>

    <article class="item" style="top:617px">
      <div class="item__head"><h2 class="item__name">LE BENEDICT SALMON</h2><span class="item__price">$14</span></div>
      <p class="item__desc" style="margin-top:13px">Savor the classic elegance of Eggs Benedict, featuring two perfectly poached eggs nestled on toasted English muffins, with luscious smoked salmon and ripe tomato slices crowned with a velvety lemon-infused Hollandaise sauce. A timeless brunch delight crafted to perfection.</p>
    </article>

    <article class="item" style="top:702px">
      <div class="item__head"><h2 class="item__name">SALMON ATLANTIQUE</h2><span class="item__price">$14</span></div>
      <p class="item__desc" style="margin-top:13px">Enjoy a bed of crisp mixed greens adorned with delicate smoked salmon, sweet golden raisins, creamy goat cheese, and crunchy walnuts. All dressed in a tantalizing balsamic vinaigrette that ties the elements together perfectly.</p>
    </article>

    <article class="item" style="top:780px">
      <div class="item__head"><h2 class="item__name">BEEF BOURGUIGNON</h2><span class="item__price">$18</span></div>
      <p class="item__desc" style="margin-top:13px">Savor the classic elegance of Eggs Benedict, featuring two perfectly poached eggs nestled on toasted English muffins, with luscious smoked salmon and ripe tomato slices crowned with a velvety lemon-infused Hollandaise sauce. A timeless brunch delight crafted to perfection.</p>
    </article>

    <article class="item" style="top:864px">
      <div class="item__head"><h2 class="item__name">TOURTE AU POULET</h2><span class="item__price">$15</span></div>
      <p class="item__desc" style="margin-top:13px">Discover the indulgent flavors of our Tourte au Poulet, a savory delight that marries tender marinated chicken with the richness of Swiss cheese and the sweetness of onions, all encased in layers of flaky pastry. Topped with a savory mushroom medley and decadent bechamel sauce. A true comfort classic to delight your senses.</p>
    </article>
  </section>

  <!-- Drinks side -->
  <section class="panel panel--drinks" aria-label="Drink specials menu">
    <div class="backdrop" role="img" aria-label="Faint Eiffel Tower silhouettes in the background"></div>
    <div class="skyline" role="img" aria-label="Red Paris skyline silhouette along the bottom edge"></div>

    <div class="frame">
      <svg width="286" height="40" viewBox="0 0 286 40" aria-hidden="true">
        <g stroke="#e2b85a" stroke-width="1" fill="none">
          <line x1="0" y1="37" x2="37" y2="0"/><line x1="0" y1="24" x2="24" y2="0"/>
          <line x1="286" y1="37" x2="249" y2="0"/><line x1="286" y1="24" x2="262" y2="0"/>
        </g>
      </svg>
    </div>

    <div class="brand"><span class="brand__mark"></span><span class="brand__name">LUEUR DE PROVINS</span></div>

    <h1 class="title"><span class="title__lead">DRINK</span><span class="title__sub">SPECIALS</span></h1>
    <div class="menu-word">MENU</div>

    <article class="item" style="top:290px">
      <div class="item__head"><h2 class="item__name">BOTTOMLESS MIMOSA</h2><span class="item__price">$18</span></div>
      <p class="item__desc">Embark on an endless journey of delight with our Bottomless Mimosa, featuring Marlowe champagne, infusing each sip with a sparkling sensation. Tailor your experience with your preferred flavor profile - opt for the timeless twist of classic orange juice or tangy cranberry juice for a refreshing zing. Continuously poured to ensure your glass is always full.</p>
    </article>

    <article class="item" style="top:379px">
      <div class="item__head"><h2 class="item__name">APPLE CIDER-MIMOSA</h2><span class="item__price">$15</span></div>
      <p class="item__desc">A delightful twist on the classic mimosa. Crafted with champagne and crisp apple cider. To elevate the experience, we adorn the glass with a caramel rim dipped in brown sugar, adding a touch of indulgent sweetness to every sip.</p>
    </article>

    <article class="item" style="top:444px">
      <div class="item__head"><h2 class="item__name item__name--wide">BLOOD ORANGE OR PINEAPPLE SPRITZ</h2><span class="item__price">$14</span></div>
      <p class="item__desc" style="margin-top:6px">Introducing our vibrant spritz cocktail, a tantalizing blend of Fenn &amp; Rowe's premium Velmora Vodka, sweet vermouth, and a touch of sweetness from a carefully muddled sugar cube. This effervescent libation reaches new heights with the addition of bubbly Clairbrook, your choice of either Blood Orange or Pineapple syrup injects a burst of fruity allure into every sip.</p>
    </article>

    <article class="item" style="top:530px">
      <div class="item__head"><h2 class="item__name">PEACH BELLINI</h2><span class="item__price">$14</span></div>
      <p class="item__desc" style="margin-top:9px">Try our perfectly balanced Peach Bellini with each sip you capture the crispness of champagne with the irresistible sweetness of peach. It's a sublime fusion of sophistication and sweetness.</p>
    </article>

    <article class="item" style="top:599px">
      <div class="item__head"><h2 class="item__name">ESPRESSO MARTINI</h2><span class="item__price">$14</span></div>
      <p class="item__desc" style="margin-top:9px">Our Espresso Martini is a decadent blend of bold espresso, rich chocolate martini, and luxurious Castellane chocolate syrup. It's the ultimate indulgence for coffee and chocolate lovers alike.</p>
    </article>

    <article class="item" style="top:669px">
      <div class="item__head"><h2 class="item__name">KIR ROYALE</h2><span class="item__price">$18</span></div>
      <p class="item__desc" style="margin-top:8px">Our Kir Royale is a delightful fusion of the crisp, sparkling champagne bubbles and the sweet sophistication of black currant. a luxurious and indulgent drink that's perfect for any occasion.</p>
    </article>

    <h3 class="section-label" style="top:732px">LATTE</h3>

    <article class="item" style="top:756px">
      <div class="item__head"><h2 class="item__name">TRUFFLE LATTE</h2><span class="item__price">$15</span></div>
      <p class="item__desc" style="margin-top:8px">We start with rich Castellane chocolate, known for its velvety smoothness and intense flavor. Then, we add a drizzle of salted caramel, adding a perfect balance of sweetness and a hint of savory richness. Finally, we combine this delightful blend with perfectly steamed milk to create a creamy and indulgent latte that will satisfy even the most discerning palate.</p>
    </article>

    <article class="item" style="top:846px">
      <div class="item__head"><h2 class="item__name">NAPOLEON LATTE</h2><span class="item__price">$15</span></div>
      <p class="item__desc" style="margin-top:8px">We start with our rich espresso, renowned for its bold and robust character. Then, we add a luscious combination of hazelnut and vanilla syrup, creating a symphony of sweetness and nutty richness. As the final touch, we crown this masterpiece with the velvety smoothness of perfectly steamed milk</p>
    </article>

    <article class="item" style="top:928px">
      <div class="item__head"><h2 class="item__name">CHAI LATTE</h2><span class="item__price">$15</span></div>
      <p class="item__desc" style="margin-top:10px">Our robust chai tea concentrate, infused with a symphony of cinnamon, cardamom, cloves, and ginger, sets the stage for a journey of aromatic delight. Paired with velvety steamed milk, each sip offers a harmonious blend of bold spices and creamy richness. Topped with a sprinkle of cinnamon, it's the perfect finishing touch to this comforting treat.</p>
    </article>
  </section>

</main>
</body>
</html>
```